Power Generation Company needs a stationary design

We need a design for our letter envelope, A4 Envelope and letterhead. Our company name is BRIXENergy which i attached here sample our our call card. We are based in the Philippines and is into the Power Generation business. We own power facilities like Hydropower plant, Solar Power Plant, Diesel Power Plant, Gas Turbine Power Plant. We sell our power to various electric distribution companies, factories and office buildings.

Target Market(s)

Electric Distribution Companies and Factories

Industry/Entity Type

It Company

Colors
ec1f27

Requirements
Must have
• Logo and company name
Nice to have
• No specific
Should not have
• No specific

```html
<!DOCTYPE html>
<html lang="en">
<head>
<meta charset="utf-8">
<title>BRIXENergy Letterhead</title>
<link rel="stylesheet" href="https://fonts.googleapis.com/css2?family=PT+Sans+Narrow:wght@400;700&display=swap">
<style>
  :root {
    --brand-red: #ec1f27;
    --deep-red: #c8151c;
    --steel-grey: #9a9a9a;
    --light-grey: #dcdcdc;
    --ink: #333333;
    --paper: #ffffff;
    --backdrop: #eaa99f;
    --watermark: #f5e2e1;
  }
  * { box-sizing: border-box; margin: 0; padding: 0; }
  html, body { width: 1200px; height: 784px; overflow: hidden; }
  body {
    background: var(--backdrop);
    font-family: "PT Sans Narrow", "Arial Narrow", sans-serif;
    color: var(--ink);
    position: relative;
  }
  .letterhead {
    position: absolute;
    left: 338px; top: 22px;
    width: 523px; height: 740px;
    background: var(--paper);
    overflow: hidden;
  }
  /* header */
  .header-bar-red {
    position: absolute; left: 40px; top: 14px;
    width: 120px; height: 6px;
    background: linear-gradient(90deg, var(--brand-red), #f4525a);
  }
  .header-bar-grey {
    position: absolute; right: 0; top: 150px;
    width: 130px; height: 6px;
    background: linear-gradient(90deg, #c9c9c9, var(--steel-grey));
  }
  .brand {
    position: absolute; right: 52px; top: 72px;
    display: flex; align-items: center; gap: 10px;
  }
  .brand-dot {
    width: 22px; height: 22px; border-radius: 50%;
    background: var(--brand-red);
  }
  .brand-name {
    font-size: 36px; font-weight: 700; color: var(--brand-red);
    letter-spacing: 1px;
  }
  .services {
    position: absolute; right: 24px; top: 122px;
    display: flex; gap: 8px;
    font-size: 9.5px; font-style: italic;
  }
  .services li { list-style: none; display: flex; align-items: center; gap: 3px; }
  .services li::before {
    content: ""; width: 0; height: 0;
    border-left: 5px solid var(--brand-red);
    border-top: 3px solid transparent; border-bottom: 3px solid transparent;
  }
  /* watermark */
  .watermark {
    position: absolute; left: 50%; top: 340px;
    transform: translateX(-50%);
    display: flex; align-items: center; gap: 14px;
    white-space: nowrap;
  }
  .watermark-ring {
    width: 72px; height: 72px; border-radius: 50%;
    border: 3px solid var(--watermark);
    flex: none;
  }
  .watermark-name {
    font-size: 64px; font-weight: 400; color: var(--watermark);
    letter-spacing: 3px;
  }
  /* contact footer */
  .contact {
    position: absolute; left: 28px; bottom: 42px; right: 28px;
    font-size: 9.5px;
  }
  .contact-tab {
    position: absolute; right: 0; top: -34px;
    background: var(--light-grey);
    color: var(--brand-red); font-weight: 700; font-size: 10.5px;
    padding: 4px 14px;
    border-left: 3px solid var(--brand-red);
    border-right: 3px solid var(--brand-red);
  }
  .contact-rule {
    position: absolute; left: 0; right: 120px; top: -20px;
    height: 1px; background: var(--light-grey);
  }
  .contact-row { display: flex; gap: 18px; margin-bottom: 7px; align-items: center; }
  .contact-item { display: flex; align-items: center; gap: 5px; white-space: nowrap; }
  .contact-icon { width: 10px; height: 10px; flex: none; }
  .footer-band-grey {
    position: absolute; left: 0; bottom: 10px;
    width: 70%; height: 7px;
    background: linear-gradient(90deg, var(--steel-grey), #c4c4c4);
    clip-path: polygon(0 0, 97% 0, 100% 100%, 0 100%);
  }
  .footer-band-red {
    position: absolute; left: 0; bottom: 0;
    width: 100%; height: 10px;
    background: linear-gradient(90deg, var(--brand-red) 70%, #f46a70);
  }
</style>
</head>
<body>
<main class="letterhead">
  <header>
    <div class="header-bar-red"></div>
    <div class="brand">
      <span class="brand-dot"></span>
      <span class="brand-name">BRIXENergy</span>
    </div>
    <ul class="services">
      <li>Hydropower plant</li>
      <li>Solar Power Plant</li>
      <li>Diesel Power Plant</li>
      <li>Gas Turbine Power Plant</li>
    </ul>
    <div class="header-bar-grey"></div>
  </header>

  <div class="watermark" aria-hidden="true">
    <span class="watermark-ring"></span>
    <span class="watermark-name">BRIXENergy</span>
  </div>

  <footer class="contact">
    <div class="contact-tab">Contact Detail</div>
    <div class="contact-rule"></div>
    <div class="contact-row">
      <span class="contact-item">
        <svg class="contact-icon" viewBox="0 0 10 10"><circle cx="5" cy="5" r="5" fill="#ec1f27"/><path d="M5 2.2a1.9 1.9 0 0 1 1.9 1.9C6.9 5.6 5 7.8 5 7.8S3.1 5.6 3.1 4.1A1.9 1.9 0 0 1 5 2.2z" fill="#fff"/></svg>
        402 Harbor Point Tower, 88 Narra Ave, Riverside Business Park, Santa Elena, Laguna City, 4020 Philippines
      </span>
    </div>
    <div class="contact-row">
      <span class="contact-item">
        <svg class="contact-icon" viewBox="0 0 10 10"><circle cx="5" cy="5" r="5" fill="#ec1f27"/><rect x="3" y="3" width="4" height="4" rx="0.6" fill="#fff"/></svg>
        +632 555 0148
      </span>
      <span class="contact-item">
        <svg class="contact-icon" viewBox="0 0 10 10"><circle cx="5" cy="5" r="5" fill="#ec1f27"/><rect x="2.8" y="3.4" width="4.4" height="3.4" rx="0.5" fill="#fff"/></svg>
        +632 555 0172
      </span>
      <span class="contact-item">
        <svg class="contact-icon" viewBox="0 0 10 10"><circle cx="5" cy="5" r="5" fill="#ec1f27"/><rect x="3.6" y="2.3" width="2.8" height="5.4" rx="0.5" fill="#fff"/></svg>
        +63 917 555 0193
      </span>
    </div>
    <div class="contact-row">
      <span class="contact-item">
        <svg class="contact-icon" viewBox="0 0 10 10"><circle cx="5" cy="5" r="5" fill="#ec1f27"/><rect x="2.6" y="3.3" width="4.8" height="3.4" fill="#fff"/><path d="M2.6 3.3 5 5.2l2.4-1.9" stroke="#ec1f27" stroke-width="0.6" fill="none"/></svg>
        mreyes@brixenergy-ph.com
      </span>
      <span class="contact-item">
        <svg class="contact-icon" viewBox="0 0 10 10"><circle cx="5" cy="5" r="5" fill="#ec1f27"/><circle cx="5" cy="5" r="2.6" fill="none" stroke="#fff" stroke-width="0.7"/><path d="M2.4 5h5.2M5 2.4v5.2" stroke="#fff" stroke-width="0.6"/></svg>
        www.brixenergy-ph.com
      </span>
    </div>
  </footer>
  <div class="footer-band-grey"></div>
  <div class="footer-band-red"></div>
</main>
</body>
</html>
```